Brent's Custom Signs and Woodworking Business Card

I run a small business that does custom woodworking and sign making. I have a logo already that I am very fond of, and would like to continue with the theme of the logo. I'd like a business card that adds onto that theme/design and stands out among typical business cards. As you'll be able to see from the logo, we're a patriotic brand and that is paramount to us.
Contact Information for Business Card
beneath the Brent's logo, I'd like it to say
"Custom Signs & Woodworking"
Also, I'd like the following information template present on the card, preferably with the logos of instagram and facebook present besides the title.
(Name)                                 (Instragram)
(Email)                                  (Facebook)
(Phone)                                 (Website)
I would like for the name, email, and phone number to be editable so that I can have my employees utilize this card design as well. but for my card, my information is as follows
Tom "Brent" Kellerby, CEO                                           @BrentsCrafted
Tom@BrentsCrafted.example                                          Brent's Crafted
(555) 014-2273                                                         BrentsCrafted.example
As for the back side, either a full american flag, or something that catches the eye, designer's preference I suppose.
Font styles to use
Other font styles liked:
- Funkydori, an adobe typekit font. it is the same as used for the logo. I'm not sure how the whole card will look with that, so if it doesn't look right please use something that complements the script style of the logo

```html
<!DOCTYPE html>
<html lang="en">
<head>
<meta charset="utf-8">
<title>Brent's Custom Signs and Woodworking — Business Card</title>
<link rel="stylesheet" href="https://fonts.googleapis.com/css2?family=Crimson+Text:wght@400;700&family=Lato:wght@400&display=swap">
<style>
  :root {
    --navy: #222d6b;
    --red: #b71f2e;
    --white: #ffffff;
    --ink: #1d1d1d;
    --stage: #3a3a3a;
    --flag-blue: #aeb0c9;
    --flag-peach: #eccdbe;
    --flag-white: #f6f4f3;
  }
  * { box-sizing: border-box; margin: 0; padding: 0; }
  html, body { width: 1200px; height: 880px; overflow: hidden; }
  body {
    background: var(--stage);
    display: flex;
    flex-direction: column;
    align-items: center;
    justify-content: center;
    gap: 50px;
  }
  .card {
    position: relative;
    width: 630px;
    height: 360px;
    border-radius: 22px;
    overflow: hidden;
    background: var(--white);
  }

  /* Back side */
  .card-back .flag-field {
    position: absolute; inset: 0;
    background:
      linear-gradient(115deg, var(--flag-blue) 0%, var(--flag-blue) 38%, var(--flag-white) 45%, var(--flag-peach) 58%, var(--flag-white) 70%, var(--flag-peach) 82%, var(--flag-white) 92%);
  }
  .back-brand {
    position: absolute;
    left: 0; right: 0; top: 95px;
    text-align: center;
  }
  .brand-name {
    font-family: "Crimson Text", serif;
    font-weight: 700;
    color: var(--navy);
    line-height: 1;
  }
  .back-brand .brand-name { font-size: 84px; }
  .tagline {
    font-family: "Lato", sans-serif;
    color: var(--ink);
  }
  .back-brand .tagline { font-size: 17px; margin-top: 6px; }
  .back-web {
    margin-top: 34px;
    font-family: "Crimson Text", serif;
    font-size: 18px;
    letter-spacing: 6px;
    color: var(--ink);
  }

  /* Front side */
  .front-waves { position: absolute; inset: 0; }
  .front-brand {
    position: absolute;
    left: 50px; top: 110px;
  }
  .front-brand .brand-name { font-size: 84px; }
  .front-brand .tagline { font-size: 16px; margin-top: 4px; padding-left: 28px; }
  .holder {
    position: absolute;
    right: 40px; top: 30px;
    text-align: right;
    font-family: "Crimson Text", serif;
    color: var(--navy);
  }
  .holder-name { font-size: 22px; font-weight: 700; }
  .holder-title { font-size: 16px; color: var(--ink); line-height: 1; }
  .contact-list {
    position: absolute;
    right: 22px; top: 168px;
    list-style: none;
    font-family: "Crimson Text", serif;
    font-size: 15px;
    color: var(--white);
  }
  .contact-list li {
    display: flex;
    justify-content: flex-end;
    align-items: center;
    gap: 8px;
    height: 23px;
  }
  .contact-icon { width: 16px; height: 16px; flex: none; }
</style>
</head>
<body>

  <section class="card card-back" aria-label="Card back">
    <div class="flag-field" role="img" aria-label="Faded waving American flag with stars and stripes"></div>
    <div class="back-brand">
      <div class="brand-name">Brent's</div>
      <div class="tagline">Custom Signs &amp; Woodworking</div>
      <div class="back-web">BrentsCrafted.example</div>
    </div>
  </section>

  <section class="card card-front" aria-label="Card front">
    <svg class="front-waves" viewBox="0 0 630 360" width="630" height="360" aria-hidden="true">
      <path d="M0,360 L0,330 C140,322 250,300 300,250 C340,205 360,160 410,130 C470,100 560,96 630,94 L630,360 Z" fill="var(--navy)"/>
      <path d="M90,356 C240,340 310,305 345,255 C378,200 395,155 440,128 C500,104 570,100 622,100" fill="none" stroke="var(--white)" stroke-width="5" stroke-linecap="round"/>
      <path d="M0,300 C150,296 250,285 300,235 C275,285 170,315 0,322 Z" fill="var(--red)"/>
    </svg>

    <div class="holder">
      <div class="holder-name">Tom "Brent" Kellerby</div>
      <div class="holder-title">CEO</div>
    </div>

    <div class="front-brand">
      <div class="brand-name">Brent's</div>
      <div class="tagline">Custom Signs &amp; Woodworking</div>
    </div>

    <ul class="contact-list">
      <li>(555) 014-2273
        <svg class="contact-icon" viewBox="0 0 16 16" aria-hidden="true"><circle cx="8" cy="8" r="7.2" fill="none" stroke="#fff" stroke-width="1.2"/><path d="M5,4.5 L6.5,4.5 L7,6.5 L6,7.3 C6.6,8.6 7.4,9.4 8.7,10 L9.5,9 L11.5,9.5 L11.5,11 C8,11.3 4.7,8 5,4.5 Z" fill="#fff"/></svg>
      </li>
      <li>Tom@BrentsCrafted.example
        <svg class="contact-icon" viewBox="0 0 16 16" aria-hidden="true"><circle cx="8" cy="8" r="7.2" fill="none" stroke="#fff" stroke-width="1.2"/><rect x="4" y="5.2" width="8" height="5.6" fill="none" stroke="#fff" stroke-width="1"/><path d="M4,5.2 L8,8.4 L12,5.2" fill="none" stroke="#fff" stroke-width="1"/></svg>
      </li>
      <li>@BrentsCrafted
        <svg class="contact-icon" viewBox="0 0 16 16" aria-hidden="true"><circle cx="8" cy="8" r="7.2" fill="none" stroke="#fff" stroke-width="1.2"/></svg>
      </li>
      <li>Brent's Crafted
        <svg class="contact-icon" viewBox="0 0 16 16" aria-hidden="true"><circle cx="8" cy="8" r="7.2" fill="none" stroke="#fff" stroke-width="1.2"/></svg>
      </li>
      <li>BrentsCrafted.example
        <svg class="contact-icon" viewBox="0 0 16 16" aria-hidden="true"><circle cx="8" cy="8" r="7.2" fill="none" stroke="#fff" stroke-width="1.2"/><circle cx="8" cy="8" r="4" fill="none" stroke="#fff" stroke-width="1"/><path d="M4,8 H12 M8,4 V12" stroke="#fff" stroke-width="1"/></svg>
      </li>
    </ul>
  </section>

</body>
</html>
```